Dance Music Album cover

We need an album cover for the release of our artist Velvetmoonz

for Velvetmoonz for his 4 tracks.

The following mentions are required for Velvetmoonz's cover :

- Velvetmoonz

- Sky on fire

- TRK47 (not mandatory)

• benny kostrin feel, Pale Orbit Records feel, Ka Ru feel to it.

```html
<!DOCTYPE html>
<html lang="en">
<head>
<meta charset="utf-8">
<title>Velvetmoonz – Sky on fire</title>
<link rel="stylesheet" href="https://fonts.googleapis.com/css2?family=Dosis:wght@300;400&family=Orbitron:wght@700&display=swap">
<style>
  :root {
    --bg-dark: #2a0000;
    --bg-mid: #7a0000;
    --bg-bright: #b80000;
    --artist: #ffffff;
    --title: #c9a293;
    --code: #6e1010;
    --figure-black: #0d0505;
    --figure-red: #d81a10;
    --figure-pink: #e0206a;
    --figure-cream: #e8ddc8;
  }
  html, body {
    margin: 0;
    padding: 0;
    overflow: hidden;
  }
  .cover {
    position: relative;
    width: 1200px;
    height: 1200px;
    overflow: hidden;
    background: linear-gradient(90deg, var(--bg-dark) 0%, var(--bg-mid) 35%, var(--bg-bright) 70%, var(--bg-bright) 100%);
  }
  .dancer-art {
    position: absolute;
    left: 430px;
    top: 0;
    width: 640px;
    height: 1200px;
  }
  .artist-name {
    position: absolute;
    left: 106px;
    top: 540px;
    margin: 0;
    font-family: "Dosis", sans-serif;
    font-weight: 400;
    font-size: 96px;
    line-height: 1;
    letter-spacing: 1px;
    color: var(--artist);
  }
  .release-title {
    position: absolute;
    left: 182px;
    top: 632px;
    margin: 0;
    font-family: "Dosis", sans-serif;
    font-weight: 300;
    font-size: 112px;
    line-height: 1;
    letter-spacing: 1px;
    text-transform: uppercase;
    color: var(--title);
    white-space: nowrap;
  }
  .catalogue-code {
    position: absolute;
    right: 58px;
    bottom: 34px;
    margin: 0;
    font-family: "Orbitron", sans-serif;
    font-weight: 700;
    font-size: 26px;
    color: var(--code);
  }
</style>
</head>
<body>
  <main class="cover">
    <svg class="dancer-art" viewBox="0 0 640 1200" role="img" aria-label="Posterised illustration of a dancer with raised arm and flying hair, in red, black, pink and cream tones">
      <defs>
        <linearGradient id="dancer-tones" x1="0" y1="0" x2="0" y2="1">
          <stop offset="0" stop-color="var(--figure-black)"/>
          <stop offset="0.35" stop-color="var(--figure-red)"/>
          <stop offset="0.6" stop-color="var(--figure-black)"/>
          <stop offset="0.8" stop-color="var(--figure-pink)"/>
          <stop offset="1" stop-color="var(--figure-red)"/>
        </linearGradient>
      </defs>
      <path d="M60 0 H400 L520 60 L600 440 L620 820 L560 1200 H340 L220 960 L230 760 L300 560 L110 470 L40 300 Z" fill="url(#dancer-tones)" opacity="0.85"/>
    </svg>

    <h1 class="artist-name">Velvetmoonz</h1>
    <h2 class="release-title">Sky on fire</h2>
    <p class="catalogue-code">TRK47</p>
  </main>
</body>
</html>
```